Poetry Book Cover Design Project

Looking for a minimalistic book cover design for a collection of poems. The book title is "Before The Morning Turns To Glass". There are three parts to the book. First covers poetry in the theme of Rage. Second love and desire. The third is strange poems. Essentially the sections are "Rage", "Desire" and the "Strange". The reason for the title "Before The Morning Turns To Glass" is as if someone is writing these till life changes towards the intended outcome as felt in each poem. I want to have the author's name "Nirosha Kulathunge" at the bottom. Ilustration attached.
- Minimalistic

```html
<!DOCTYPE html>
<html lang="en">
<head>
<meta charset="utf-8">
<title>Before The Morning Turns To Glass — Cover Wrap</title>
<link href="https://fonts.googleapis.com/css2?family=Special+Elite&family=EB+Garamond&display=swap" rel="stylesheet">
<style>
  :root {
    --stage: #ececec;
    --paper: #ffffff;
    --ink: #1a1a1a;
    --art-red: #e0343a;
    --art-orange: #d9773f;
    --art-cream: #f4ece4;
    --art-cyan: #43c6e0;
    --art-navy: #2b3f6b;
  }
  * { margin: 0; padding: 0; box-sizing: border-box; }
  html, body {
    width: 899px; height: 1200px; overflow: hidden;
    background: var(--stage);
  }
  .cover-wrap {
    position: absolute;
    left: 11px; top: 296px;
    width: 877px; height: 608px;
    background: var(--paper);
    box-shadow: 0 2px 6px rgba(0,0,0,0.18);
    overflow: hidden;
  }
  .back-blurb {
    position: absolute;
    left: 42px; top: 81px; width: 316px;
    font-family: "EB Garamond", serif;
    font-size: 9.8px; line-height: 12.8px;
    color: var(--ink);
    text-align: justify;
  }
  .spine-title, .spine-author {
    position: absolute;
    font-family: "Special Elite", monospace;
    color: var(--ink);
    white-space: nowrap;
    transform-origin: left top;
    transform: rotate(90deg);
  }
  .spine-title { left: 456px; top: 56px; font-size: 9.5px; }
  .spine-author { left: 459px; top: 358px; font-size: 15px; }
  .front-author {
    position: absolute;
    left: 497px; top: 58px;
    font-family: "Special Elite", monospace;
    font-size: 15px; letter-spacing: 0.3px;
    color: var(--ink);
  }
  .front-title {
    position: absolute;
    right: 32px; top: 36px;
    z-index: 2;
    font-family: "Special Elite", monospace;
    font-size: 28px; line-height: 31px;
    font-weight: 400;
    text-align: right;
    color: var(--ink);
  }
  .front-title span { display: block; }
  .paint-art {
    position: absolute;
    left: 515px; top: 262px;
    width: 362px; height: 346px;
    z-index: 1;
    border-radius: 48% 0 0 0 / 40% 0 0 0;
    background:
      radial-gradient(ellipse at 30% 85%, rgba(255,255,255,0.7), rgba(255,255,255,0) 45%),
      linear-gradient(100deg, var(--art-red) 0%, var(--art-orange) 28%, var(--art-cream) 52%, var(--art-cyan) 76%, var(--art-navy) 100%);
    opacity: 0.9;
  }
</style>
</head>
<body>
  <main class="cover-wrap">
    <p class="back-blurb">Lorem ipsum dolor sit amet, consectetur adipiscing elit. Donec ligula magna, tempus eu auctor sit amet, pharetra ut velit. Curabitur euismod congue nibh quis feugiat. Vivamus in neque in erat lacinia consectetur. In a rhoncus metus. Sed fringilla eros tellus, finibus lobortis libero mattis ut. Maecenas urna neque, porttitor in mi et, porttitor auctor enim. Donec auctor at dolor sit amet dapibus. Proin luctus imperdiet nisi, in semper dui molestie vitae. Sed semper hendrerit tempor. Phasellus velit est, accumsan et molestie ut, condimentum ac erat. Nam aliquam ultricies leo vitae dictum. Morbi non nisi nec nisl vulputate imperdiet in in purus.</p>

    <div class="spine-title">Before The Morning Turns To Glass</div>
    <div class="spine-author">Nirosha Kulathunge</div>

    <div class="front-author">Nirosha Kulathunge</div>
    <h1 class="front-title">
      <span>Before</span>
      <span>The</span>
      <span>Morning</span>
      <span>Turns</span>
      <span>To</span>
      <span>Glass</span>
    </h1>

    <div class="paint-art" role="img" aria-label="Abstract fluid paint splash in red, orange, cream, cyan and navy with scattered droplets"></div>
  </main>
</body>
</html>
```